Vell Partners Building Business Cards

We need a business card that reflects our business as "Solar Experts" in San Diego. Browse our website www.vellpartners.example our License needs to be displayed as "CSLB# 4718392" our phone number is (619) 555-0147

Save thousands on your electric bills and increase the value of your home while helping to protect the environment. Our solar installation experts will help you design the system that's right for you, using only the highest quality equipment that will look great and give you ideal performance. Our goal is to make you energy independent, and get your electric bill to 0.

Tobias Wrenfield
(619) 555-0147
tobias@vellpartners.example

Target Market(s)

Home owners in san diego looking for solar

Industry/Entity Type

Solar Energy

Contact Information for Business Card

Tobias Wrenfield
(619) 555-0147
tobias@vellpartners.example

Font styles to use
Other font styles liked:
• Use our logo font

Requirements
Must have
• License needs to be displayed as "CSLB# 4718392" our phone number is (619) 555-0147
Nice to have
• Real images of rooftop home solar in san diego
Should not have
• our business address

```html
<!DOCTYPE html>
<html lang="en">
<head>
<meta charset="utf-8">
<title>Vell Partners Building – Business Cards</title>
<link rel="stylesheet" href="https://fonts.googleapis.com/css2?family=Cinzel:wght@500&family=Roboto:wght@400;700&family=Tinos:ital@1&display=swap">
<style>
  :root {
    --navy: #1b3a78;
    --navy-light: #24468a;
    --gold: #f5ac0a;
    --white: #ffffff;
    --page: #e7e8ea;
  }
  * { margin: 0; padding: 0; box-sizing: border-box; }
  html, body { width: 1200px; height: 1000px; overflow: hidden; background: var(--page); }
  .card {
    position: absolute; left: 220px; width: 760px;
    box-shadow: 0 6px 18px rgba(0,0,0,.25); overflow: hidden;
  }
  .card--front {
    top: 50px; height: 433px;
    background: linear-gradient(115deg, var(--navy) 0%, var(--navy) 55%, var(--navy-light) 100%);
  }
  .card--back { top: 523px; height: 437px; background: var(--white); }

  .wordmark {
    font-family: "Roboto", Arial, sans-serif; font-weight: 700;
    letter-spacing: -0.5px; white-space: nowrap;
  }
  .card--front .wordmark {
    position: absolute; top: 190px; left: 0; right: 0; text-align: center;
    font-size: 46px; color: var(--white);
  }
  .tagline {
    position: absolute; top: 352px; left: 0; right: 0; text-align: center;
    font-family: "Tinos", "Times New Roman", serif; font-style: italic;
    font-size: 27px; color: var(--white); letter-spacing: .5px;
  }
  .license {
    position: absolute; top: 395px; left: 0; right: 0; text-align: center;
    font-family: "Roboto", Arial, sans-serif; font-size: 14px;
    color: var(--gold); letter-spacing: 1px;
  }
  .card--back .wordmark {
    position: absolute; top: 68px; left: 40px;
    font-size: 37px; color: var(--navy);
  }
  .wave { position: absolute; inset: 0; }
  .edge-tab {
    position: absolute; right: 0; top: 262px; width: 11px; height: 40px;
    background: var(--gold); border-radius: 5px 0 0 5px;
  }
  .person { position: absolute; right: 44px; top: 258px; text-align: right; }
  .person__name {
    font-family: "Cinzel", Georgia, serif; font-weight: 500;
    font-size: 23px; color: var(--gold); letter-spacing: 1.5px;
  }
  .person__role {
    font-family: "Roboto", Arial, sans-serif; font-size: 17px; color: var(--white); margin-top: 2px;
  }
  .contact {
    position: absolute; right: 44px; top: 326px; list-style: none;
    font-family: "Roboto", Arial, sans-serif; font-size: 17px; color: var(--white);
  }
  .contact li {
    display: flex; justify-content: flex-end; align-items: center;
    height: 24px; gap: 10px;
  }
  .contact svg { width: 14px; height: 14px; flex: none; }
</style>
</head>
<body>

<section class="card card--front">
  <div class="wordmark">Vell Partners Building Inc</div>
  <p class="tagline">The Solar Experts</p>
  <p class="license">CSLB# 4718392</p>
</section>

<section class="card card--back">
  <div class="wordmark">Vell Partners Building Inc</div>
  <svg class="wave" viewBox="0 0 760 437" preserveAspectRatio="none" aria-hidden="true">
    <path fill="var(--gold)" d="M0,148 C80,225 170,268 270,258 C390,246 470,140 560,132 C640,125 715,160 760,200 L760,437 L0,437 Z"/>
    <path fill="var(--navy)" d="M0,178 C90,245 180,272 280,264 C395,254 475,146 565,138 C645,131 718,166 760,210 L760,437 L0,437 Z"/>
  </svg>
  <div class="edge-tab"></div>
  <div class="person">
    <div class="person__name">Tobias Wrenfield</div>
    <div class="person__role">President</div>
  </div>
  <ul class="contact">
    <li>(619) 555-0147
      <svg viewBox="0 0 14 14"><path fill="var(--gold)" d="M3 1l2.5 2.5-1.3 1.6c.8 1.7 2 2.9 3.7 3.7l1.6-1.3L12 10l-1.6 2.4C6 12 2 8 1.6 2.6z"/></svg>
    </li>
    <li>tobias@vellpartners.example
      <svg viewBox="0 0 14 14"><rect x="1" y="3" width="12" height="9" fill="var(--gold)"/><path d="M1 3l6 5 6-5" fill="none" stroke="var(--navy)" stroke-width="1.2"/></svg>
    </li>
    <li>www.vellpartners.example
      <svg viewBox="0 0 14 14"><circle cx="7" cy="7" r="6" fill="var(--gold)"/><path d="M1 7h12M7 1c-2.5 3-2.5 9 0 12M7 1c2.5 3 2.5 9 0 12" fill="none" stroke="var(--navy)" stroke-width="0.9"/></svg>
    </li>
  </ul>
</section>

</body>
</html>
```